New Innovative Counselling and psychotherapy Service needs Business Card design

Keep it simple and professional. On one side, just company name and logo (perhaps in all blue) and maybe a tag line.

On other side (all white) my name and Qualifications in centre

Industry/Entity Type

Health And Wellness

Contact Information for Business Card

Derek Hollis
Counsellor & Psychotherapist
BSc (Psychol.), BA, Dip. (Couns. & Psych.), PG.Cert (CBT), MGVrA, NWTF

I will also require Mobile no, Email and web site address of which I'll pass on to final designer.

Font styles to use
Sans Serif

Requirements
Must have
• My Logo Only and please use the colours in logo that is in it.
Should not have
• Any other images

```html
<!DOCTYPE html>
<html lang="en">
<head>
<meta charset="utf-8">
<title>Clearwell Path – Business Card</title>
<link rel="stylesheet" href="https://fonts.googleapis.com/css2?family=Open+Sans:wght@400;600;700&display=swap">
<style>
  :root {
    --backdrop: #2a2a2c;
    --brand-blue: #41ade6;
    --brand-blue-deep: #35a0da;
    --brand-green: #8dc63f;
    --card-white: #ffffff;
    --text-grey: #4a4a4a;
    --text-dark: #222222;
    --rule-grey: #555555;
  }
  * { box-sizing: border-box; margin: 0; padding: 0; }
  html, body {
    width: 1200px; height: 1141px; overflow: hidden;
    background: var(--backdrop);
    font-family: "Open Sans", Arial, sans-serif;
  }
  .canvas {
    position: relative; width: 1200px; height: 1141px;
    display: flex; flex-direction: column; align-items: center; justify-content: center; gap: 60px;
  }
  .card {
    width: 760px; height: 434px; position: relative; overflow: hidden;
    box-shadow: 0 10px 30px rgba(0,0,0,.45);
  }
  /* Front side */
  .card--front {
    background: var(--brand-blue);
  }
  .card__pattern {
    position: absolute; inset: 0;
    background: linear-gradient(135deg, var(--brand-blue) 0%, var(--brand-blue-deep) 100%);
  }
  .brand {
    position: absolute; left: 50%; top: 50%; transform: translate(-50%, -50%);
    display: flex; align-items: center; gap: 18px;
  }
  .brand__dot {
    width: 58px; height: 58px; border-radius: 50%; background: var(--card-white);
  }
  .brand__name {
    color: var(--card-white); font-weight: 600; font-size: 38px; letter-spacing: .2px;
  }
  /* Back side */
  .card--back {
    background: var(--card-white);
    display: flex; align-items: center; justify-content: center;
  }
  .profile {
    text-align: right; padding-right: 28px;
  }
  .profile__name {
    color: var(--brand-blue); font-weight: 700; font-size: 30px; line-height: 1.2; margin-bottom: 4px;
  }
  .profile__line {
    color: var(--text-grey); font-size: 17px; line-height: 1.45;
  }
  .divider {
    width: 2px; height: 120px; background: var(--rule-grey);
  }
  .contacts {
    list-style: none; padding-left: 26px;
  }
  .contacts__item {
    display: flex; align-items: center; gap: 12px;
    color: var(--text-dark); font-size: 17px; line-height: 1.75;
  }
  .contacts__icon { width: 18px; height: 18px; flex: none; }
  .contacts__icon * { fill: none; stroke: var(--brand-green); stroke-width: 2; stroke-linejoin: round; stroke-linecap: round; }
  .contacts__icon .solid { fill: var(--brand-green); stroke: none; }
</style>
</head>
<body>
<main class="canvas">
  <section class="card card--front" aria-label="Card front">
    <div class="card__pattern" role="img" aria-label="Subtle repeating brand pattern in tones of blue"></div>
    <div class="brand">
      <span class="brand__dot"></span>
      <span class="brand__name">Clearwell Path</span>
    </div>
  </section>

  <section class="card card--back" aria-label="Card back">
    <div class="profile">
      <h1 class="profile__name">Derek Hollis</h1>
      <p class="profile__line">Counsellor &amp; Psychotherapist</p>
      <p class="profile__line">BSc (Psychol.), BA, Dip. (Couns.</p>
      <p class="profile__line">&amp; Psych.), PG.Cert (CBT), MGVrA, NWTF</p>
    </div>
    <div class="divider"></div>
    <ul class="contacts">
      <li class="contacts__item">
        <svg class="contacts__icon" viewBox="0 0 18 18" aria-hidden="true"><path class="solid" d="M3 2l3 0 1.5 4-2 1.3a9 9 0 0 0 5.2 5.2l1.3-2 4 1.5v3a1.5 1.5 0 0 1-1.6 1.5A14 14 0 0 1 1.5 3.6 1.5 1.5 0 0 1 3 2z"/></svg>
        <span>+61 85550 2741</span>
      </li>
      <li class="contacts__item">
        <svg class="contacts__icon" viewBox="0 0 18 18" aria-hidden="true"><rect x="5" y="2" width="8" height="4"/><rect x="2" y="6" width="14" height="7" rx="1"/><rect x="5" y="11" width="8" height="5"/></svg>
        <span>08-5550-2741</span>
      </li>
      <li class="contacts__item">
        <svg class="contacts__icon" viewBox="0 0 18 18" aria-hidden="true"><rect x="2" y="4" width="14" height="10"/><path d="M2 4l7 6 7-6"/></svg>
        <span>info@clearwellpath.com.au</span>
      </li>
      <li class="contacts__item">
        <svg class="contacts__icon" viewBox="0 0 18 18" aria-hidden="true"><circle cx="9" cy="9" r="7"/><ellipse cx="9" cy="9" rx="3" ry="7"/><path d="M2 9h14"/></svg>
        <span>www.clearwellpath.com.au</span>
      </li>
    </ul>
  </section>
</main>
</body>
</html>
```